Corporate brochure design 4 pages

Hi,

We are a real estate company based in Europe.

We have almost finalized a rebranding.

We are developing a brand book guidelines (still on working process) to help you undertstand the look and feel of our new CI. I would like to receive proposals of design for a corporate brochure template. I need to receive the Indesign files with full ownership rights to be able to adapt all our documentation with this template.
Regarding the images, you can take gabaris on www.pelvaromedia.com. I will be able to take them afterwards.

There will be 4 pages. you will receive the 4 pages on pdf for your consideration with our (almost) actual layout.

- 1st page: cover
- 2nd page: company presentation in french and english
- 3rd page: some market data + graph
- 4th page: 2 retail centers presentation.

In the template, i need to have:
- the paragraph styles in order
- 2 different masters with top/bottom/page number aso.

Please feel free to ask any other questions.

best regards,
Updates

I would like to precise tha t we are active on the commercial real estate sector:

- office transactions (rent /sales)
- property management of administrative and business buildings
- Valuation of properties
- Capital markets (investment advices for selling building)

Industry/Entity Type

Real Estate

Colors

Designer to choose colors to be used in the design.

```html
<!DOCTYPE html>
<html lang="en">
<head>
<meta charset="utf-8">
<title>Meridian – Corporate Brochure, 4 Pages</title>
<link rel="stylesheet" href="https://fonts.googleapis.com/css2?family=Open+Sans:wght@400;600;700&display=swap">
<style>
  :root {
    --brand-blue: #2f7aa5;
    --brand-blue-dark: #1f5f86;
    --brand-grey: #6e6f73;
    --grey-light: #8b8c90;
    --ink: #2b2b2b;
    --rule: #c9d3db;
    --row-alt: #eef3f7;
    --paper: #ffffff;
    --canvas: #ffffff;
  }
  * { box-sizing: border-box; margin: 0; padding: 0; }
  html, body { width: 1200px; height: 900px; overflow: hidden; background: var(--canvas); }
  body { font-family: "Open Sans", Arial, sans-serif; color: var(--ink); position: relative; }

  .page {
    position: absolute; top: 278px; width: 236px; height: 336px;
    background: var(--paper); overflow: hidden;
    box-shadow: 0 4px 10px rgba(0,0,0,.28);
  }
  .page--cover { left: 92px; }
  .page--about { left: 348px; }
  .page--market { left: 618px; }
  .page--retail { left: 868px; }

  .page-shapes { position: absolute; inset: 0; width: 100%; height: 100%; }

  .running-head {
    position: absolute; top: 20px; right: 12px;
    font-size: 5.5px; color: var(--brand-grey); display: flex; align-items: baseline; gap: 4px;
  }
  .running-head .folio { font-size: 8px; color: var(--ink); }

  /* Cover */
  .cover-photo {
    position: absolute; left: 0; top: 0; width: 236px; height: 306px;
    background: linear-gradient(160deg, #8fa9cc 0%, #4e6fa8 35%, #2b4a8a 65%, #5877a8 100%);
  }
  .cover-logo {
    position: absolute; right: 0; bottom: 0; width: 108px; height: 52px; background: var(--paper);
    display: flex; align-items: center; justify-content: center;
  }
  .cover-logo span { font-size: 11px; font-weight: 700; letter-spacing: .5px; color: #1d1d1f; }

  /* About */
  .about-columns { position: absolute; left: 44px; top: 86px; right: 12px; height: 154px; display: flex; gap: 10px; overflow: hidden; }
  .about-col { flex: 1; min-width: 0; }
  .section-title { font-size: 9.5px; font-weight: 700; color: var(--brand-blue); margin-bottom: 5px; }
  .body-copy { font-size: 3.9px; line-height: 1.38; color: var(--ink); margin-bottom: 3.5px; text-align: justify; }
  .about-photo { position: absolute; top: 244px; width: 86px; height: 66px; }
  .about-photo--glass { left: 26px; background: linear-gradient(150deg, #b9d3ea, #3b6c9f 60%, #23507c); }
  .about-photo--sign { left: 126px; background: linear-gradient(170deg, #5b8ed0, #8fb6e4 70%, #cfdcea); }

  /* Market */
  .market-columns { position: absolute; left: 32px; top: 38px; right: 10px; display: flex; gap: 10px; }
  .market-col { flex: 1; min-width: 0; }
  .market-col .section-title { font-size: 10px; margin-bottom: 3px; }
  .market-col .body-copy { font-size: 4px; }
  .table-title { font-size: 4.6px; color: var(--brand-blue); font-weight: 600; margin: 4px 0 2px; }
  .data-table { width: 100%; border-collapse: collapse; font-size: 2.8px; margin-bottom: 3px; }
  .data-table th { background: #d8e4ee; color: var(--brand-blue-dark); text-align: left; padding: .6px 2px; font-weight: 600; }
  .data-table td { padding: .55px 2px; border-bottom: .4px solid var(--rule); }
  .data-table tr:nth-child(even) td { background: var(--row-alt); }
  .data-table .total td { font-weight: 600; border-bottom: none; }
  .grand-total { display: flex; gap: 26px; font-size: 5px; color: var(--brand-blue); border-top: .6px solid var(--brand-blue); padding-top: 2px; margin-top: 4px; }
  .grand-total span:last-child { font-size: 3.5px; color: var(--ink); }
  .chart-caption { font-size: 2.6px; text-align: center; color: var(--brand-grey); margin: 4px 0 1px; }
  .market-photo { width: 100%; height: 50px; margin-top: 8px; }
  .market-photo--office { background: linear-gradient(180deg, #cfe3f5 0%, #9fc2e0 45%, #6f8ea6 70%, #b9c0c4 100%); }
  .market-photo--house { background: linear-gradient(180deg, #e4edf5 0%, #c8d6e2 50%, #a7a9a5 80%, #d3d3cf 100%); }

  /* Retail */
  .retail-heading {
    position: absolute; left: 8px; color: #fff; font-size: 6.4px; font-weight: 600; line-height: 1.25;
  }
  .retail-heading--first { top: 8px; }
  .retail-heading--second { top: 178px; }
  .retail-info { position: absolute; left: 46px; right: 8px; }
  .retail-info--first { top: 44px; }
  .retail-info--second { top: 206px; }
  .info-row { display: flex; gap: 4px; border-bottom: .5px solid var(--brand-blue); padding: 1.2px 0; font-size: 3px; }
  .info-row dt { width: 46px; flex: none; font-weight: 600; color: var(--brand-blue-dark); }
  .info-row dd { flex: 1; line-height: 1.35; }
  .retail-map { position: absolute; left: 46px; width: 44px; height: 34px; background: radial-gradient(circle at 50% 50%, #d6d8db, #b7babe 70%, transparent 72%); }
  .retail-map--first { top: 100px; }
  .retail-map--second { top: 262px; }
</style>
</head>
<body>

<!-- Page 1 · Cover -->
<section class="page page--cover" aria-label="Cover">
  <div class="cover-photo" role="img" aria-label="Photo of a curved glass office tower against a blue sky"></div>
  <svg class="page-shapes" viewBox="0 0 236 336" aria-hidden="true">
    <polygon points="236,188 236,336 0,336 0,306" fill="#6e6f73"/>
    <polygon points="236,152 236,188 0,306 0,290" fill="#55565a"/>
  </svg>
  <div class="cover-logo"><span>MERIDIAN</span></div>
</section>

<!-- Page 2 · About us -->
<section class="page page--about" aria-label="About us">
  <svg class="page-shapes" viewBox="0 0 236 336" aria-hidden="true">
    <polygon points="0,0 236,0 236,5 28,50 32,336 0,336" fill="#2f7aa5"/>
  </svg>
  <div class="running-head"><span>About us /&nbsp; A Propos De Nous</span><span class="folio">2</span></div>
  <div class="about-columns">
    <article class="about-col">
      <h2 class="section-title">A Team</h2>
      <p class="body-copy">Our ambition is to offer quality services that perfectly meet your expectations. This ambition is shared by all members of the team.</p>
      <p class="body-copy">Thanks to our knowledge of the Luxembourg market, our skills and our commitment to the missions entrusted to us, Halden Partners is the undisputed leader in commercial real estate in the Grand Duchy. We are proud of this position and work hard to deserve it every day.</p>
      <p class="body-copy">Targeting excellence means the constant improvement of our services in order to more accurately meet your needs. When you meet with us, you will find that our employees take the necessary time to listen to you and to understand your need. Their professionalism and know-how will ensure that we find the right solution.</p>
    </article>
    <article class="about-col" lang="fr">
      <h2 class="section-title">Une Équipe</h2>
      <p class="body-copy">Proposer des services de qualité répondant parfaitement à vos attentes est notre ambition. Elle est partagée par tous les membres de notre équipe.</p>
      <p class="body-copy">Notre connaissance du marché luxembourgeois, nos compétences et notre engagement font de Halden Partners l'acteur majeur de l'immobilier d'entreprise au Grand-Duché. Nous sommes fiers de cette position et travaillons tous les jours pour la conserver.</p>
      <p class="body-copy">Viser l'excellence suppose d'améliorer sans cesse nos services afin de mieux répondre à vos besoins. Nos collaborateurs prennent le temps de vous écouter pour bien comprendre votre demande. Leur savoir-faire nous permettra de trouver la solution.</p>
    </article>
  </div>
  <div class="about-photo about-photo--glass" role="img" aria-label="Photo of glass office facades seen from below"></div>
  <div class="about-photo about-photo--sign" role="img" aria-label="Photo of a blank property sign post against the sky"></div>
</section>

<!-- Page 3 · Market data -->
<section class="page page--market" aria-label="Market data">
  <svg class="page-shapes" viewBox="0 0 236 336" aria-hidden="true">
    <polygon points="0,0 22,0 24,336 0,336" fill="#8b8c90"/>
  </svg>
  <div class="running-head"><span>Halden Partners</span><span class="folio">3</span></div>
  <div class="market-columns">
    <div class="market-col" lang="fr">
      <h2 class="section-title">Stock</h2>
      <p class="body-copy">Le stock de mètres carrés disponibles de bureaux a augmenté de 0,36 % au troisième trimestre de cette année grâce à la livraison de près de 12 300 m². Le stock total équivaut à 3 465 600 m².</p>

      <h3 class="table-title">Centre - Ville (City)</h3>
      <table class="data-table">
        <tr><th>Quartiers - Districts</th><th>Stock m²</th><th>Stock %</th></tr>
        <tr><td>Kirchberg</td><td>652 900</td><td>18,84 %</td></tr>
        <tr><td>CBD</td><td>456 500</td><td>13,17 %</td></tr>
        <tr><td>Station</td><td>382 700</td><td>11,04 %</td></tr>
        <tr><td>Cloche d'Or</td><td>357 600</td><td>10,32 %</td></tr>
        <tr><td>Limpertsberg</td><td>85 300</td><td>2,46 %</td></tr>
        <tr><td>Belair / Merl</td><td>84 100</td><td>2,43 %</td></tr>
        <tr><td>Hamm</td><td>44 100</td><td>1,27 %</td></tr>
        <tr><td>Hollerich</td><td>33 000</td><td>0,95 %</td></tr>
        <tr class="total"><td>Total</td><td>2 096 200</td><td>60,48 %</td></tr>
      </table>

      <h3 class="table-title">Ville Périphérie (City-Periphery)</h3>
      <table class="data-table">
        <tr><th>Quartiers - Districts</th><th>Stock m²</th><th>Stock %</th></tr>
        <tr><td>Howald</td><td>237 500</td><td>6,85 %</td></tr>
        <tr><td>Bertrange</td><td>96 200</td><td>2,78 %</td></tr>
        <tr><td>Strassen</td><td>90 300</td><td>2,61 %</td></tr>
        <tr><td>Leudelange</td><td>56 800</td><td>1,64 %</td></tr>
        <tr class="total"><td>Total</td><td>480 800</td><td>13,88 %</td></tr>
      </table>

      <h3 class="table-title">Périphérie (Periphery)</h3>
      <table class="data-table">
        <tr><th>Quartiers - Districts</th><th>Stock m²</th><th>Stock %</th></tr>
        <tr><td>Munsbach</td><td>224 600</td><td>6,48 %</td></tr>
        <tr><td>Capellen</td><td>165 500</td><td>4,78 %</td></tr>
        <tr><td>Windhof</td><td>119 900</td><td>3,46 %</td></tr>
        <tr><td>Contern</td><td>105 100</td><td>3,03 %</td></tr>
        <tr><td>Foetz</td><td>92 500</td><td>2,67 %</td></tr>
        <tr><td>Mamer</td><td>90 200</td><td>2,60 %</td></tr>
        <tr><td>Bettembourg</td><td>90 800</td><td>2,62 %</td></tr>
        <tr class="total"><td>Total</td><td>888 600</td><td>25,64 %</td></tr>
      </table>
      <div class="grand-total"><span>Total</span><span>3 465 600</span></div>
    </div>

    <div class="market-col">
      <h2 class="section-title">Stock</h2>
      <p class="body-copy">The stock of available office square meters has increased by 0.36% during the third quarter of this year with the delivery of 12,300 m². The total stock reaches 3,465,600 m².</p>
      <p class="chart-caption">Evolution of office stock (m²)</p>
      <svg viewBox="0 0 90 46" width="90" height="46" role="img" aria-label="Bar chart of office stock growth over twelve years">
        <line x1="4" y1="2" x2="4" y2="40" stroke="#c9d3db" stroke-width=".4"/>
        <line x1="4" y1="40" x2="88" y2="40" stroke="#9aa3aa" stroke-width=".4"/>
        <g stroke="#e3e8ec" stroke-width=".3">
          <line x1="4" y1="10" x2="88" y2="10"/><line x1="4" y1="20" x2="88" y2="20"/><line x1="4" y1="30" x2="88" y2="30"/>
        </g>
        <g fill="#2f7aa5">
          <rect x="6" y="28" width="5" height="12"/><rect x="13" y="26" width="5" height="14"/>
          <rect x="20" y="24" width="5" height="16"/><rect x="27" y="22" width="5" height="18"/>
          <rect x="34" y="20" width="5" height="20"/><rect x="41" y="18" width="5" height="22"/>
          <rect x="48" y="16" width="5" height="24"/><rect x="55" y="14" width="5" height="26"/>
          <rect x="62" y="13" width="5" height="27"/><rect x="69" y="12" width="5" height="28"/>
          <rect x="76" y="11" width="5" height="29"/><rect x="83" y="10" width="4" height="30"/>
        </g>
        <polyline points="8,26 15,24 22,22 29,20 36,18 43,16 50,14 57,12 64,11 71,10 78,9 85,8" fill="none" stroke="#6e6f73" stroke-width=".5"/>
        <rect x="68" y="43" width="8" height="2" fill="#2f7aa5"/>
      </svg>
      <div class="market-photo market-photo--office" role="img" aria-label="Photo of a modern glass office building under a blue sky"></div>
      <div class="market-photo market-photo--house" role="img" aria-label="Photo of a low business building with a garage"></div>
    </div>
  </div>
</section>

<!-- Page 4 · Retail centres -->
<section class="page page--retail" aria-label="Retail centres">
  <svg class="page-shapes" viewBox="0 0 236 336" aria-hidden="true">
    <polygon points="0,0 118,0 106,26 38,36 40,170 0,170" fill="#2f7aa5"/>
    <polygon points="0,176 236,176 236,180 38,198 40,336 0,336" fill="#2f7aa5"/>
    <polygon points="236,264 236,336 164,336" fill="#2f7aa5"/>
  </svg>
  <div class="running-head"><span>Retail Center</span><span class="folio">4</span></div>

  <h2 class="retail-heading retail-heading--first">High Streets Luxembourg:<br>City - Pedes - Trian zone</h2>
  <dl class="retail-info retail-info--first">
    <div class="info-row"><dt>Zone - Zone</dt><dd>Pedestrian zone Grand-Rue, Rue du Marché</dd></div>
    <div class="info-row"><dt>Stock - Stock</dt><dd>51 500 m² &nbsp; net</dd></div>
    <div class="info-row"><dt>Magasins - Shops</dt><dd>+/- 260</dd></div>
    <div class="info-row"><dt>Niveau Loyers - Rental level</dt><dd>880 – 1 100</dd></div>
    <div class="info-row"><dt>Parking</dt><dd>3 800 (public)</dd></div>
    <div class="info-row"><dt>Marques principales - Main brands</dt><dd>Fashion chains, jewellers, department store, shoe shops, cosmetics, bookshops, opticians, cafés and luxury boutiques</dd></div>
  </dl>
  <div class="retail-map retail-map--first" role="img" aria-label="Simplified city map locating the pedestrian zone"></div>

  <h2 class="retail-heading retail-heading--second">High Streets Luxembourg:<br>Station Av. Gare</h2>
  <dl class="retail-info retail-info--second">
    <div class="info-row"><dt>Zone - Zone</dt><dd>Avenue de la Gare</dd></div>
    <div class="info-row"><dt>Stock - Stock</dt><dd>17 900 m² &nbsp; net</dd></div>
    <div class="info-row"><dt>Magasins - Shops</dt><dd>+/- 110</dd></div>
    <div class="info-row"><dt>Niveau Loyers - Rental level</dt><dd>380 – 720 (market level)</dd></div>
    <div class="info-row"><dt>Parking</dt><dd>1 600 (public)</dd></div>
    <div class="info-row"><dt>Marques principales - Main brands</dt><dd>Fashion chains, shoe shops, bakeries, opticians, pharmacies, banks, cafés and discount stores</dd></div>
  </dl>
  <div class="retail-map retail-map--second" role="img" aria-label="Simplified city map locating the station avenue"></div>
</section>

</body>
</html>
```